Stationery Design Needed: Business Card, Letterhead, Folder Design

Logo files attached I plan on using the standard us folder size 9x12 as well as standard US business card and letter head. I am the owner of Harborline Restorative Spine Associates, www.harborlinespinecare.example. I now have two locations, each with the same phone number and website. I enclosed my slogan and the information. I practice in an honest, ethical manor and place patients at a top priority. I want the designs to fit with my logo which symbolizes a blend of the symbol for ethical, honesty ( the peacock ) and the medusa ( medicine ) . I want to use the colors form my website blue, grey, silver to blend in and be cohesive and also match along the modern but natural colors along with blue and grey from the office. I want my cards and stationary to stand out

Target Market(s)

Lawyers, Surgeons, Primary Care Physicians Chiropractors

Industry/Entity Type

Business

Contact Information for Business Card

I want the cards and folders to stand out ...Bold colors I like the dark blue the best as I want this to be my signature color ...See below
I don t want too much white or too much aqua blue

Colors
3277b5

Requirements
Must have
• On Business cards... Must have logo, My name and practice, Two addresses, and my certifications from anesthesia and pain medicine .... web site easy to read for my target age audience 40 +
Nice to have
• slogan and other certifications
Should not have
• Confusing small to real letters ... so may need double sides but with all important on the front

```html
<!DOCTYPE html>
<html lang="en">
<head>
<meta charset="utf-8">
<title>Harborline Restorative Spine Associates – Business Card</title>
<link rel="stylesheet" href="https://fonts.googleapis.com/css2?family=Arimo:ital,wght@0,400;0,700;1,400&display=swap">
<style>
  :root {
    --page-bg: #e9ecef;
    --card-white: #ffffff;
    --blue-deep: #1f8fd6;
    --blue-bright: #2aa8e6;
    --blue-light: #8fd3f4;
    --blue-pale: #dff2fb;
    --brand-blue: #3277b5;
    --text-grey: #5a5f66;
  }
  * { box-sizing: border-box; margin: 0; padding: 0; }
  html, body {
    width: 1200px; height: 950px; overflow: hidden;
    background: var(--page-bg);
    font-family: "Arimo", Arial, sans-serif;
  }
  .sheet {
    width: 1200px; height: 950px;
    display: flex; flex-direction: column; align-items: center; justify-content: center;
    gap: 50px;
  }
  .card {
    position: relative;
    width: 700px; height: 400px;
    background: var(--card-white);
    overflow: hidden;
    box-shadow: 0 4px 14px rgba(0,0,0,0.12);
  }
  .card-front .backdrop { position: absolute; inset: 0; }
  .card-front .illustration {
    position: absolute; left: 20px; top: 150px;
    width: 330px; height: 230px;
    border-radius: 50% 50% 40% 40%;
    background: radial-gradient(ellipse at center, var(--blue-pale) 0%, rgba(223,242,251,0.4) 60%, rgba(255,255,255,0) 75%);
  }
  .front-details {
    position: absolute; right: 40px; top: 36px;
    width: 340px; color: var(--card-white); text-align: right;
  }
  .doctor-name { font-size: 27px; font-weight: 700; letter-spacing: 0.3px; }
  .credentials { margin-top: 10px; list-style: none; font-size: 10.5px; line-height: 1.45; font-weight: 700; }
  .locations { margin-top: 22px; font-size: 14px; line-height: 1.5; }
  .locations address { font-style: normal; }
  .locations address + address { margin-top: 6px; }
  .phones { margin-top: 10px; font-size: 14px; font-weight: 700; letter-spacing: 0.3px; }

  .card-back {
    display: flex; flex-direction: column; align-items: center; justify-content: center;
  }
  .brand {
    display: flex; align-items: center; gap: 18px;
  }
  .brand-dot {
    width: 64px; height: 64px; border-radius: 50%;
    background: var(--blue-bright);
    flex: none;
  }
  .brand-name {
    font-size: 34px; font-weight: 700; color: var(--blue-bright);
    line-height: 1.1; width: 420px;
  }
  .slogan {
    margin-top: 34px;
    font-size: 17px; font-style: italic; color: var(--text-grey);
  }
  .website {
    margin-top: 10px; font-size: 17px; font-weight: 700; color: var(--brand-blue);
  }
</style>
</head>
<body>
<main class="sheet">
  <section class="card card-front">
    <svg class="backdrop" viewBox="0 0 700 400" preserveAspectRatio="none" aria-hidden="true">
      <defs>
        <linearGradient id="frontBlue" x1="0" y1="0" x2="1" y2="1">
          <stop offset="0" stop-color="#2aa8e6"/>
          <stop offset="0.55" stop-color="#1f8fd6"/>
          <stop offset="1" stop-color="#1a7cc6"/>
        </linearGradient>
      </defs>
      <path d="M0 0 H700 V400 H430 C430 260 360 150 0 120 Z" fill="url(#frontBlue)"/>
    </svg>
    <div class="illustration" role="img" aria-label="Large winged medical staff illustration in light blue outline"></div>
    <div class="front-details">
      <h1 class="doctor-name">Martin R. Ellsworth, D.O.</h1>
      <ul class="credentials">
        <li>Diplomate, Continental Board of Pain Practice</li>
        <li>Diplomate, Continental Board of Anesthesia Care</li>
        <li>Diplomate, Regional Osteopathic Licensing Council</li>
        <li>Adjunct Faculty Westbrook College of Osteopathic Medicine</li>
        <li>CPPS Certified in Controlled Dangerous Substances</li>
        <li>CPPS Certified in Fluoroscopic Interpretation &amp; Radiation Safety</li>
      </ul>
      <div class="locations">
        <address>4180 Palisade Ave<br>Weston Heights, N.J. 07091</address>
        <address>2250 Rt. 9 West, Suite 110<br>Brookfield, N.J. 07022</address>
      </div>
      <p class="phones">P: 201-555-0142 &nbsp;F: 201-555-0143</p>
    </div>
  </section>

  <section class="card card-back">
    <div class="brand">
      <span class="brand-dot" aria-hidden="true"></span>
      <h2 class="brand-name">Harborline Restorative Spine Associates</h2>
    </div>
    <p class="slogan">Steady Care Built on Skill &amp; Trust</p>
    <p class="website">www.harborlinespinecare.example</p>
  </section>
</main>
</body>
</html>
```